Window Perf design with eadership quotes

I am wanting to create a window perf that covers windows in a conference room. I have included a picture of the windows. Each window is 26 1/2 inches by 92 inches. I have also included several other pictures to give an example of how I would like the Quotes to look.

Some Quotes I would like to use
1. Your Future is created by what you do today not tomorrow.
2. The answer is Yes
3. People don't care how much you know until they know how much you care.
4. Treat employees like they make a difference and they will.
5. Don't follow the crowd, Let the crowd follow you.
6. Treat people as if they were what they ought to be , and help them become what they are capable of being.
7. Leadership is not a title, its a behavior. LIVE IT
8. We make a living by what we get, We make a life by what we give.
9. Success is not final, failure is not fatal: it is courage to continue that counts.
10. The best way to predict your future is to create it.
11. The supreme quality of leadership is Integrity.
12. Whatever you are, Be a good one

Quotes

• I am imore interested in how this looks rather than including all of the quotes. I also ant this to be a solid background design for privacy.

```html
<!DOCTYPE html>
<html lang="en">
<head>
<meta charset="utf-8">
<title>Leadership Quotes – Window Perf Panels</title>
<link href="https://fonts.googleapis.com/css2?family=Montserrat:ital,wght@0,400;0,600;0,700;0,800;1,600;1,700;1,800&family=Playfair+Display:ital,wght@0,400;0,700;0,900;1,400;1,700;1,900&family=Alfa+Slab+One&family=Oswald:wght@500;700&family=Pinyon+Script&family=Josefin+Sans:wght@300;400;700&display=swap" rel="stylesheet">
<style>
  :root{
    --backdrop:#7b8f8e;
    --panel:#0b0b0e;
    --white:#ffffff;
    --red:#e5202b;
    --sage:#8a9c98;
    --wine:#6d1d24;
  }
  *{box-sizing:border-box;margin:0;padding:0}
  html,body{width:1200px;height:1000px;overflow:hidden;background:var(--backdrop)}
  .canvas{position:relative;width:1200px;height:1000px;background:var(--backdrop)}
  .panel{position:absolute;top:24px;height:961px;background:var(--panel);color:var(--white);overflow:hidden}
  .panel--1{left:24px;width:282px}
  .panel--2{left:328px;width:262px}
  .panel--3{left:610px;width:263px}
  .panel--4{left:895px;width:281px}
  .quote{position:absolute;left:0;right:0;text-align:center}
  .line{display:block;white-space:nowrap}
  .sans{font-family:'Montserrat',sans-serif}
  .geo{font-family:'Josefin Sans',sans-serif}
  .serif{font-family:'Playfair Display',serif}
  .slab{font-family:'Alfa Slab One',serif}
  .cond{font-family:'Oswald',sans-serif}
  .script{font-family:'Pinyon Script',cursive}
  .red{color:var(--red)}
  .sage{color:var(--sage)}
  .ital{font-style:italic}

  /* Panel 1 */
  .q-future{top:40px}
  .q-future .your{font:400 27px/1 'Montserrat',sans-serif;letter-spacing:14px;padding-left:14px}
  .q-future .future{font:800 34px/1 'Montserrat',sans-serif;letter-spacing:3px;margin-top:10px;transform:scaleX(1.15)}
  .q-future .created{font:700 27px/1 'Montserrat',sans-serif;margin-top:8px}
  .q-future .created i{font-style:italic;font-weight:700;font-size:24px}
  .q-future .whatdo{font:400 31px/1 'Josefin Sans',sans-serif;margin-top:12px}
  .q-future .today{font:800 32px/1 'Montserrat',sans-serif;margin-top:8px;display:flex;justify-content:center;align-items:center;gap:6px}
  .q-future .today svg{display:block}
  .q-future .tomorrow{font:400 26px/1 'Josefin Sans',sans-serif;margin-top:10px;display:flex;justify-content:center;align-items:center;gap:4px;padding-right:8px}
  .q-future .not{font:700 11px/1 'Montserrat',sans-serif;color:var(--red);transform:rotate(-90deg);display:inline-block;width:14px}
  .q-future .strike{text-decoration:line-through;text-decoration-color:var(--red);text-decoration-thickness:3px}

  .q-yes{top:360px;padding:0 26px}
  .q-yes .bar{height:8px;background:var(--white)}
  .q-yes .the{font:400 34px/1 'Playfair Display',serif;letter-spacing:18px;margin-top:20px;padding-left:14px}
  .q-yes .answer{font:400 33px/1 'Alfa Slab One',serif;letter-spacing:4px;margin-top:10px}
  .q-yes .is-row{display:flex;align-items:center;gap:10px;margin-top:8px}
  .q-yes .rules{flex:1;display:flex;flex-direction:column;gap:3px}
  .q-yes .rules span{height:2px;background:var(--white)}
  .q-yes .is{font:400 32px/1 'Josefin Sans',sans-serif;letter-spacing:6px}
  .q-yes .yes{font:400 76px/1 'Alfa Slab One',serif;letter-spacing:4px;margin:6px 0 14px}

  .q-employees{top:712px}
  .q-employees .treat{font:900 27px/1 'Playfair Display',serif;font-style:italic;text-align:left;padding-left:54px}
  .q-employees .emp{font:400 22px/1 'Josefin Sans',sans-serif;letter-spacing:5px;margin-top:12px}
  .q-employees .like{font:italic 400 25px/1 'Playfair Display',serif;margin-top:8px}
  .q-employees .like b{font-weight:900;color:var(--sage);font-size:30px}
  .q-employees .diff{font:700 27px/1 'Montserrat',sans-serif;margin-top:10px}
  .q-employees .will{font:italic 900 27px/1 'Playfair Display',serif;margin-top:6px}
  .q-employees .will .amp{font-size:40px;color:var(--white)}
  .q-employees .will .sage{border-bottom:3px solid var(--sage);border-radius:0 0 40px 0;padding-right:8px}

  /* Panel 2 */
  .q-care{top:48px}
  .q-care .a{font:400 26px/1.35 'Playfair Display',serif}
  .q-care .b{font:400 25px/1.35 'Playfair Display',serif;letter-spacing:5px}
  .q-care .c{font:700 26px/1.35 'Playfair Display',serif;letter-spacing:1px}
  .q-care .d{font:italic 400 27px/1.35 'Playfair Display',serif}

  .q-crowd{top:370px}
  .q-crowd .l1{font:italic 800 22px/1 'Montserrat',sans-serif}
  .q-crowd .l1 span{font-weight:400}
  .q-crowd .l2{font:400 18px/1 'Montserrat',sans-serif;letter-spacing:3px;margin-top:8px}
  .q-crowd .l2 b{font-weight:800;font-size:27px;letter-spacing:0;color:var(--red)}
  .q-crowd .l3{font:400 23px/1 'Montserrat',sans-serif;margin-top:8px}
  .q-crowd .l3 small{font-size:14px}
  .q-crowd .follow{font:italic 900 27px/1 'Playfair Display',serif;letter-spacing:2px;text-align:left;padding-left:38px;margin-top:6px}
  .q-crowd .path{display:block;margin:-4px 0 0 46px}
  .q-crowd .you{font:italic 900 44px/1 'Playfair Display',serif;position:absolute;left:104px;top:152px}

  .q-give{top:672px}
  .q-give .spaced{font:400 25px/1 'Josefin Sans',sans-serif;letter-spacing:7px}
  .q-give .bold{font:italic 900 34px/1.15 'Playfair Display',serif}
  .q-give .get{font:italic 900 30px/1 'Playfair Display',serif;margin-bottom:8px}
  .q-give .get b{font:700 38px/1 'Oswald',sans-serif;font-style:normal;color:var(--sage)}
  .q-give .give{font:italic 900 30px/1 'Playfair Display',serif;display:flex;justify-content:center;align-items:flex-end;gap:8px}
  .q-give .give b{font:700 72px/0.9 'Oswald',sans-serif;font-style:normal;color:var(--sage)}

  /* Panel 3 */
  .q-good{top:54px}
  .q-good .whatever{font:700 32px/1 'Montserrat',sans-serif;letter-spacing:4px}
  .q-good .youare{font:400 24px/1 'Montserrat',sans-serif;letter-spacing:4px;margin-top:8px;display:flex;justify-content:center;align-items:center;gap:4px}
  .q-good .be{font:400 50px/1 'Alfa Slab One',serif;letter-spacing:14px;margin-top:8px;transform:scaleX(1.35)}
  .q-good .agood{font:italic 900 32px/1 'Playfair Display',serif;margin-top:2px;padding-left:52px}
  .q-good .one{font:400 42px/1 'Alfa Slab One',serif;color:var(--red);letter-spacing:4px;padding-left:100px;margin-top:2px}
  .q-good .helmet{position:absolute;left:22px;top:140px;width:84px;height:78px;border-radius:42px 42px 14px 30px;background:linear-gradient(135deg,#fff,#cfd3d3)}

  .q-success{top:340px}
  .q-success .big{font:700 36px/1 'Montserrat',sans-serif;letter-spacing:6px}
  .q-success .small{font:300 24px/1 'Josefin Sans',sans-serif;letter-spacing:3px;margin:8px 0}
  .q-success .small b{font-weight:700;color:var(--sage)}
  .q-success .courage{font:400 16px/1 'Josefin Sans',sans-serif;margin-top:4px}
  .q-success .courage b{font-size:30px;font-weight:400}
  .q-success .cont{font:italic 400 17px/1 'Josefin Sans',sans-serif;margin-top:6px}
  .q-success .cont b{font-style:normal;font-size:20px;letter-spacing:3px;font-weight:400}
  .q-success .counts{font:800 34px/1 'Montserrat',sans-serif;color:var(--sage);letter-spacing:7px;margin-top:12px}

  .q-leader{top:656px;padding:0 36px}
  .q-leader .rules{display:flex;flex-direction:column;gap:4px}
  .q-leader .rules span{height:2px;background:var(--white)}
  .q-leader .crown-row{display:flex;align-items:center;gap:8px}
  .q-leader .crown-row .rules{flex:1}
  .q-leader .crown{width:44px;height:40px;background:linear-gradient(#fff,#dcdcdc);border-radius:4px 4px 2px 2px}
  .q-leader .title1{font:700 30px/1 'Montserrat',sans-serif;letter-spacing:2px;margin-top:14px}
  .q-leader .title2{font:italic 400 20px/1 'Playfair Display',serif;margin-top:10px}
  .q-leader .title2 b{font:italic 400 26px/1 'Josefin Sans',sans-serif;letter-spacing:4px}
  .q-leader .title3{font:italic 400 20px/1 'Playfair Display',serif;margin-top:8px}
  .q-leader .title3 b{font:italic 400 24px/1 'Josefin Sans',sans-serif;letter-spacing:1px}
  .q-leader .live{font:700 48px/1 'Josefin Sans',sans-serif;letter-spacing:6px;margin:12px 0 10px}

  /* Panel 4 */
  .q-integrity{top:44px}
  .q-integrity .the{font:400 28px/1 'Playfair Display',serif;letter-spacing:22px;padding-left:22px}
  .q-integrity .supreme{font:700 34px/1 'Playfair Display',serif;color:var(--sage);letter-spacing:3px;margin-top:2px}
  .q-integrity .quality{font:400 46px/0.8 'Pinyon Script',cursive;margin-top:2px}
  .q-integrity .leadership{font:400 26px/1 'Playfair Display',serif;letter-spacing:2px;margin-top:8px}
  .q-integrity .is{font:400 24px/1 'Playfair Display',serif;letter-spacing:4px;margin-top:4px}
  .q-integrity .integrity{font:400 48px/1 'Oswald',sans-serif;color:var(--sage);letter-spacing:8px;margin-top:6px;font-weight:500;transform:scaleX(0.9)}

  .q-capable{top:330px}
  .q-capable .it{font:italic 700 23px/1.15 'Playfair Display',serif}
  .q-capable .be-row{font:italic 700 23px/1 'Playfair Display',serif;display:flex;justify-content:center;align-items:flex-end;gap:4px}
  .q-capable .be-row b{font:italic 900 46px/0.8 'Playfair Display',serif;border-bottom:2px solid var(--white)}
  .q-capable .help-row{display:flex;justify-content:center;align-items:center;gap:4px;margin-top:2px}
  .q-capable .help-row .help{font:italic 900 42px/1 'Playfair Display',serif;border-top:2px solid var(--white)}
  .q-capable .help-row small{font:italic 700 20px/1 'Playfair Display',serif}
  .q-capable .being{font:italic 900 40px/1 'Playfair Display',serif;margin-top:4px}

  .q-predict{top:670px}
  .q-predict .the{font:400 22px/1 'Montserrat',sans-serif;letter-spacing:10px;padding-left:10px}
  .q-predict .best{font:700 24px/1 'Montserrat',sans-serif;letter-spacing:6px;margin-top:12px}
  .q-predict .to{font:400 16px/1 'Montserrat',sans-serif;margin-top:10px}
  .q-predict .to b{font:italic 800 26px/1 'Montserrat',sans-serif;color:var(--red);letter-spacing:5px}
  .q-predict .yf{font:700 20px/1 'Montserrat',sans-serif;letter-spacing:5px;margin-top:12px}
  .q-predict .isto{font:400 20px/1 'Montserrat',sans-serif;letter-spacing:5px;margin-top:10px}
  .q-predict .created{font:400 34px/1 'Josefin Sans',sans-serif;letter-spacing:8px;color:transparent;-webkit-text-stroke:1.5px var(--wine);margin-top:18px}
  .q-predict .it2{font:700 32px/1 'Montserrat',sans-serif;letter-spacing:4px;margin-top:12px}
</style>
</head>
<body>
<main class="canvas">

  <section class="panel panel--1">
    <div class="quote q-future">
      <span class="line your">YOUR</span>
      <span class="line future red">FUTURE</span>
      <span class="line created"><i>is</i>CREATED<i>by</i></span>
      <span class="line whatdo">WHAT YOU DO</span>
      <span class="line today">
        <svg width="26" height="20" viewBox="0 0 26 20"><path d="M0 7h14V1l12 9-12 9v-6H0z" fill="var(--red)"/></svg>
        <span>T<span class="red">O</span>DAY</span>
        <svg width="26" height="20" viewBox="0 0 26 20"><path d="M26 7H12V1L0 10l12 9v-6h14z" fill="var(--red)"/></svg>
      </span>
      <span class="line tomorrow"><span class="not">NOT</span><span class="strike">TOMORROW</span></span>
    </div>

    <div class="quote q-yes">
      <div class="bar"></div>
      <span class="line the">•THE•</span>
      <span class="line answer">answer</span>
      <div class="is-row">
        <div class="rules"><span></span><span></span><span></span><span></span></div>
        <span class="is">IS</span>
        <div class="rules"><span></span><span></span><span></span><span></span></div>
      </div>
      <span class="line yes">YES</span>
      <div class="bar"></div>
    </div>

    <div class="quote q-employees">
      <span class="line treat">Treat</span>
      <span class="line emp">EMPLOYEES</span>
      <span class="line like">like <b>they</b> make a</span>
      <span class="line diff">DIFFERENCE</span>
      <span class="line will"><span class="amp">&amp;</span> <span class="sage">they will</span></span>
    </div>
  </section>

  <section class="panel panel--2">
    <div class="quote q-care">
      <span class="line a">People don’t care</span>
      <span class="line b">HOW MUCH</span>
      <span class="line c">YOU KNOW</span>
      <span class="line d">until they know</span>
      <span class="line b">HOW MUCH</span>
      <span class="line c">YOU CARE</span>
    </div>

    <div class="quote q-crowd">
      <span class="line l1">DON’T<span>FOLLOW</span></span>
      <span class="line l2">THE<b>CROWD</b></span>
      <span class="line l3">LET<small>THE</small>CROWD</span>
      <span class="line follow">FOLLOW</span>
      <svg class="path" width="170" height="50" viewBox="0 0 170 50">
        <path d="M120 2h46v16H4v28h56" fill="none" stroke="var(--red)" stroke-width="1.5" stroke-dasharray="4 3"/>
        <path d="M56 41l8 5-8 5z" fill="var(--red)"/>
      </svg>
      <span class="you">YOU</span>
    </div>

    <div class="quote q-give">
      <span class="line spaced">WE MAKE</span>
      <span class="line bold">a living by</span>
      <span class="line get">what <b>WE GET</b></span>
      <span class="line spaced">WE MAKE</span>
      <span class="line bold">a life by what</span>
      <span class="line give">we <b>GIVE</b></span>
    </div>
  </section>

  <section class="panel panel--3">
    <div class="quote q-good">
      <span class="line whatever">WHATEVER</span>
      <span class="line youare">YOU
        <svg width="22" height="22" viewBox="0 0 24 24"><path d="M12 1l3.2 7.2 7.8.7-5.9 5.2 1.8 7.7L12 17.8 5.1 21.8l1.8-7.7L1 8.9l7.8-.7z" fill="var(--red)"/></svg>
        ARE</span>
      <span class="line be">BE</span>
      <span class="line agood">a good</span>
      <span class="line one">ONE</span>
      <div class="helmet" role="img" aria-label="Football helmet illustration"></div>
    </div>

    <div class="quote q-success">
      <span class="line big">SUCCESS</span>
      <span class="line small">is<b>NOT</b>final</span>
      <span class="line big">FAILURE</span>
      <span class="line small">is<b>NOT</b>fatal:</span>
      <span class="line courage">it is <b>COURAGE</b></span>
      <span class="line cont">to<b>CONTINUE</b> that</span>
      <span class="line counts">COUNTS</span>
    </div>

    <div class="quote q-leader">
      <div class="crown-row">
        <div class="rules"><span></span><span></span><span></span></div>
        <div class="crown" role="img" aria-label="Crown emblem"></div>
        <div class="rules"><span></span><span></span><span></span></div>
      </div>
      <span class="line title1">LEADERSHIP</span>
      <span class="line title2">is not a <b>TITLE</b></span>
      <span class="line title3">it’s a <b>BEHAVIOR</b></span>
      <span class="line live">LIVE IT</span>
      <div class="rules"><span></span><span></span><span></span><span></span></div>
    </div>
  </section>

  <section class="panel panel--4">
    <div class="quote q-integrity">
      <span class="line the">THE</span>
      <span class="line supreme">SUPREME</span>
      <span class="line quality">Quality of</span>
      <span class="line leadership">LEADERSHIP</span>
      <span class="line is">IS</span>
      <span class="line integrity">INTEGRITY</span>
    </div>

    <div class="quote q-capable">
      <span class="line it">Treat people as</span>
      <span class="line it">if they were what</span>
      <span class="line be-row">they ought to <b>be</b></span>
      <span class="line help-row"><span class="help">&amp;help</span><small>them</small></span>
      <span class="line it">become what they</span>
      <span class="line it">are capable of</span>
      <span class="line being">being</span>
    </div>

    <div class="quote q-predict">
      <span class="line the">THE</span>
      <span class="line best">BEST WAY</span>
      <span class="line to">TO <b>PREDICT</b></span>
      <span class="line yf">YOUR FUTURE</span>
      <span class="line isto">IS TO</span>
      <span class="line created">CREATED</span>
      <span class="line it2">IT</span>
    </div>
  </section>

</main>
</body>
</html>
```